Stand bag for exclusive, natural snacks

We are looking for a PP stand bag design that will be used to pack exclusive snacks (dried fruits). These snacks will be 100% natural, healthy and without any chemicals. For that reason and for the fact that these products will have a higher price point, the stand bag design should look very premium and happy, while still reminding the customer of the natural, healthy benefits of the snacks inside. The main colors of our brand are black and gold, so we would like to see the packaging in similar colors. In order to be able to see the product, we usually leave some part of the PP packaging transparent.
Packaging Size: h170mm x w80mm x d30mm

Target Market(s)

High-end retail markets with consumers that are willing to pay a little more to get a high-quality product, free from any preservatives and completely natural.

Font styles to use
Sans Serif

Colors

Designer to choose colors to be used in the design.

Requirements
Must have
• - similar to the bag in the sample photos
• - bag size: h170mm x w80mm x d30mm
• - Our logo
• - the colors black & gold
• - Some way of showing the customer the benefit of our dried fruits (healthy, natural, happy)
• - a transparent part to see the product through the plastic foil
Nice to have
• - bottom maybe not transparent in order not to see dust that falls to the bottom

```html
<!DOCTYPE html>
<html lang="en">
<head>
<meta charset="utf-8">
<title>Aurelle Pantry – Dried Fruits Stand Bag</title>
<link rel="stylesheet" href="https://fonts.googleapis.com/css2?family=Libre+Baskerville:wght@700&family=Oswald:wght@300;500&display=swap">
<style>
  :root {
    --bg: #ececec;
    --black: #111111;
    --black-soft: #2a2a2a;
    --gold: #d9a81c;
    --white: #f7f7f7;
    --green: #6cc23a;
  }
  * { margin: 0; padding: 0; box-sizing: border-box; }
  html, body { width: 1154px; height: 1200px; overflow: hidden; background: var(--bg); }
  .canvas { position: relative; width: 1154px; height: 1200px; }

  .bag { position: absolute; left: 262px; top: 70px; width: 640px; height: 1060px; }

  .seal-strip { position: absolute; left: 0; top: 0; width: 640px; height: 90px; background: var(--white); border-bottom: 1px solid #d6d6d6; }

  .side-panel {
    position: absolute; left: 0; top: 90px; width: 170px; height: 970px;
    background: linear-gradient(90deg, #050505, var(--black-soft));
  }
  .front-panel {
    position: absolute; left: 170px; top: 90px; width: 470px; height: 970px;
    background: linear-gradient(160deg, #3a3a3a 0%, var(--black) 45%, #262626 100%);
  }

  .side-copy {
    position: absolute; left: 22px; top: 430px; width: 130px;
    font-family: "Oswald", sans-serif; font-weight: 300; font-size: 15px; line-height: 1.55;
    color: var(--gold); text-align: center;
  }

  .white-band { position: absolute; left: 0; top: 720px; width: 640px; height: 150px; background: var(--white); border-top: 6px solid var(--gold); border-bottom: 6px solid var(--gold); }

  .brand-name {
    position: absolute; left: 170px; top: 215px; width: 470px; text-align: center;
    font-family: "Libre Baskerville", serif; font-weight: 700; font-size: 40px; line-height: 1.2;
    color: var(--gold);
  }

  .product-title {
    position: absolute; left: 170px; top: 400px; width: 470px; text-align: center;
    font-family: "Libre Baskerville", serif; font-weight: 700; font-size: 84px; line-height: 0.95;
    color: var(--gold);
  }

  .window { position: absolute; left: 200px; top: 660px; width: 410px; height: 270px; }

  .natural-badge { position: absolute; left: 218px; top: 935px; width: 80px; height: 80px; }

  .net-weight {
    position: absolute; left: 340px; top: 945px; width: 200px; text-align: center;
    font-family: "Oswald", sans-serif; font-weight: 500; font-size: 34px; color: var(--gold);
  }
</style>
</head>
<body>
<div class="canvas">
  <div class="bag">
    <div class="seal-strip"></div>
    <div class="side-panel"></div>
    <div class="front-panel"></div>
    <div class="white-band"></div>

    <p class="side-copy">Pack of exclusive snacks (dried fruits). 100% natural, healthy and without any chemicals and free from any preservatives</p>

    <p class="brand-name">Aurelle Pantry</p>

    <h1 class="product-title">Dried<br>Fruits</h1>

    <svg class="window" viewBox="0 0 410 270">
      <defs>
        <radialGradient id="mix" cx="50%" cy="50%" r="60%">
          <stop offset="0%" stop-color="#c99a55"/>
          <stop offset="55%" stop-color="#8a4f2a"/>
          <stop offset="100%" stop-color="#4a1f1c"/>
        </radialGradient>
      </defs>
      <ellipse cx="205" cy="135" rx="200" ry="130" fill="url(#mix)" role="img" aria-label="Clear window showing the mix of raisins, walnuts, almonds, hazelnuts and dried cranberries"/>
      <ellipse cx="205" cy="135" rx="200" ry="130" fill="none" stroke="#d9a81c" stroke-width="7"/>
    </svg>

    <svg class="natural-badge" viewBox="0 0 80 80">
      <circle cx="40" cy="40" r="36" fill="none" stroke="#6cc23a" stroke-width="3"/>
    </svg>

    <p class="net-weight">500g</p>
  </div>
</div>
</body>
</html>
```